Commerical Office Furniture Company Needs Truck Wrap Design for Box Truck

We need a truck wrap design (and business card) for our company based in Fresno, California. We offer commercial office furnishings such as private office desks, cubicle stations, conference tables, all office seating (task chairs, guest, lobby/lounge, conference) storage systems, ergonomic solutions (monitor arms, keyboard trays, lift desks) and much more. We are a full service office furniture dealer who can fully outfit every space and need for a new or existing office space. We also offer design and space planning services and professional installation.
We would like our trap wrap to be modern using the same color scheme as our logo with a clean but eye catching look. Perhaps using a few nice looking desk/workstations product images as examples to show people what we are capable of. We attached some examples of some themes/layouts we like. feel free to be creative. Our website trymoldavo.com has some images and info.
https://photoshelf.brovane-co.com/detail/client-space-shared-tessel-workstation-with-q-line-storage-height-adjustable-tables-and-wexmoor-seating
Target Market(s)
Private Sector, Education, Healthcare
Industry/Entity Type
Requirements
Must have
- Dorvik Box Truck - 190 inches x 85 inches

```html
<!DOCTYPE html>
<html lang="en">
<head>
<meta charset="utf-8">
<title>Moldavo Office Interiors – Box Truck Wrap</title>
<link rel="stylesheet" href="https://fonts.googleapis.com/css2?family=Poppins:wght@400;500;600;700&display=swap">
<style>
  :root {
    --page: #eceef0;
    --wrap-white: #f4f5f6;
    --brand-blue: #0b4fd6;
    --charcoal: #3b3d40;
    --band-dark: #3e4043;
    --text-dark: #2b2d30;
    --photo-wall: #dcdcda;
    --photo-floor: #b9b6b1;
  }
  html, body {
    margin: 0;
    width: 1200px;
    height: 1200px;
    overflow: hidden;
    background: var(--page);
    font-family: "Poppins", sans-serif;
  }
  .truck-wrap {
    position: absolute;
    left: 40px;
    top: 357px;
    width: 1120px;
    height: 486px;
    display: block;
    box-shadow: 0 6px 24px rgba(0,0,0,.12);
  }
  .brand-name { font-family: "Poppins", sans-serif; font-weight: 700; fill: var(--brand-blue); }
  .company-title { font-family: "Poppins", sans-serif; font-weight: 600; fill: var(--brand-blue); }
  .company-sub { font-family: "Poppins", sans-serif; font-weight: 500; fill: var(--charcoal); letter-spacing: 4px; }
  .services { font-family: "Poppins", sans-serif; font-weight: 500; fill: var(--text-dark); }
  .phone { font-family: "Poppins", sans-serif; font-weight: 600; fill: #ffffff; letter-spacing: 1.6px; }
  .website { font-family: "Poppins", sans-serif; font-weight: 400; fill: #ffffff; letter-spacing: 1px; }
</style>
</head>
<body>
<svg class="truck-wrap" viewBox="0 0 548 238" preserveAspectRatio="none" xmlns="http://www.w3.org/2000/svg">
  <defs>
    <linearGradient id="office-photo-tone" x1="0" y1="0" x2="0" y2="1">
      <stop offset="0" stop-color="var(--photo-wall)"/>
      <stop offset="0.55" stop-color="#d3d1cd"/>
      <stop offset="0.62" stop-color="#bfa88a"/>
      <stop offset="0.72" stop-color="var(--photo-floor)"/>
      <stop offset="1" stop-color="#a9a7a3"/>
    </linearGradient>
    <linearGradient id="contact-band-fade" x1="0" y1="0" x2="1" y2="0">
      <stop offset="0" stop-color="var(--band-dark)" stop-opacity="0"/>
      <stop offset="0.22" stop-color="var(--band-dark)" stop-opacity="1"/>
      <stop offset="1" stop-color="var(--band-dark)"/>
    </linearGradient>
  </defs>

  <!-- conference room imagery area -->
  <rect class="office-photo" x="0" y="0" width="548" height="238" fill="url(#office-photo-tone)"
        role="img" aria-label="Photo of a modern conference room with a long wooden table, white task chairs and framed wall art"/>

  <!-- white brand field -->
  <path class="brand-field" d="M232 0 H548 V182 H318 Q296 182 288 162 Z" fill="var(--wrap-white)"/>

  <!-- blue diagonal sweep -->
  <path class="blue-sweep" d="M155 0 H232 L288 162 Q296 182 318 182 H548 V187 H300 Q276 187 266 166 Z" fill="var(--brand-blue)"/>

  <!-- dark contact band -->
  <rect class="contact-band" x="250" y="190" width="298" height="48" fill="url(#contact-band-fade)"/>

  <!-- brand name in logo position -->
  <text class="brand-name" x="408" y="82" font-size="44" text-anchor="middle">MOLDAVO</text>

  <text class="company-title" x="408" y="122" font-size="19" text-anchor="middle">MOLDAVO OFFICE</text>
  <line x1="285" y1="138" x2="315" y2="138" stroke="var(--charcoal)" stroke-width="1.4"/>
  <text class="company-sub" x="410" y="142" font-size="12.5" text-anchor="middle">INTERIORS</text>
  <line x1="501" y1="138" x2="531" y2="138" stroke="var(--charcoal)" stroke-width="1.4"/>
  <text class="services" x="408" y="161" font-size="8.6" text-anchor="middle">Office Furniture  •  Design  •  Installation</text>

  <text class="phone" x="305" y="212" font-size="19">559-555-0142</text>
  <text class="website" x="306" y="230" font-size="12">www.trymoldavo.com</text>
</svg>
</body>
</html>
```